Soy Candle Labels

We sell soy candles in recycled wine bottles. The wine bottle is cut in half and filled with pure and natural soy wax and scented with essential oils.
Our product represents good use of up cycling materials for a better use. The product is all natural and eco friendly.
You can see good use of labels and branding for a company in America that does the same thing http://marrowlanewicks.example/
Trya dn keep the label uncomplicated like the above labels.
We will need an area to hand stamp the scent. Similar to the labels used on the above website.
We would prefer to use a white or off white paper label with gold or bronze printing - limit the use of colour and keep the label simple and sophisticated.
Brambrel Candle Co. is our company name. Brambrel being the predominant name and candle co. written small underneath right justified.
Die cut labels might look better than a rectangle.
Dimensions should be 90mm Wide x 90mm High
The final design should communicate a professional and quality product. But stay modern and professional. Clean, elegant and sophisticated.
Can use wording such as: Hand Poured, Premium Soy Wax, All Natural, Up cycled
Have a look at the attached image for the look and feel we are going for.
Updates
Designers are having a little bit of trouble interpreting the brief into a viable design. To assist perhaps you can look at WINE LABELS on google images. Design your label around an existing style wine label to give the canld ethe feel of being a bottle of wine. Get creative! :)
Reason: We require more designs. We havnt quite got what were looking for.
Please see brief.

```html
<!DOCTYPE html>
<html lang="en">
<head>
<meta charset="utf-8">
<title>Brambrel Candle Co. – Soy Candle Label</title>
<link rel="stylesheet" href="https://fonts.googleapis.com/css2?family=Great+Vibes&family=Cinzel:wght@400&family=Bebas+Neue&display=swap">
<style>
  :root {
    --paper: #fefbe3;
    --gold: #cfb36b;
    --gold-faint: #f3e6c2;
    --ornament: #f6edcc;
    --stamp-green: #a9ba8b;
  }
  html, body {
    margin: 0;
    padding: 0;
    width: 1200px;
    height: 1200px;
    overflow: hidden;
    background: var(--paper);
  }
  .label {
    position: relative;
    width: 1200px;
    height: 1200px;
    background: var(--paper);
    overflow: hidden;
  }
  .ornament-band {
    position: absolute;
    left: 0;
    top: 207px;
    width: 1200px;
    height: 242px;
    background: linear-gradient(180deg, var(--paper) 0%, var(--ornament) 30%, var(--ornament) 70%, var(--paper) 100%);
  }
  .brand-name {
    position: absolute;
    right: 56px;
    top: 500px;
    margin: 0;
    font-family: "Great Vibes", cursive;
    font-weight: 400;
    font-size: 286px;
    line-height: 1;
    color: var(--gold);
    white-space: nowrap;
  }
  .brand-suffix {
    position: absolute;
    right: 50px;
    top: 726px;
    margin: 0;
    font-family: "Cinzel", serif;
    font-size: 44px;
    line-height: 1.2;
    letter-spacing: 1px;
    color: var(--gold);
  }
  .claims {
    position: absolute;
    right: 508px;
    top: 920px;
    margin: 0;
    font-family: "Cinzel", serif;
    font-size: 32px;
    color: var(--gold);
    white-space: nowrap;
  }
  .claims .divider {
    display: inline-block;
    margin: 0 18px;
  }
  .double-rule {
    position: absolute;
    left: 0;
    top: 984px;
    width: 692px;
    height: 3px;
    background: var(--gold);
    box-shadow: 0 8px 0 var(--gold);
  }
  .scent-caption {
    position: absolute;
    left: 830px;
    top: 1008px;
    margin: 0;
    font-family: "Cinzel", serif;
    font-size: 27px;
    color: var(--gold);
    transform: translate(-50%, -50%) rotate(-90deg);
    white-space: nowrap;
  }
  .scent-stamp {
    position: absolute;
    left: 855px;
    top: 853px;
    width: 296px;
    height: 296px;
  }
  .scent-name {
    position: absolute;
    left: 1007px;
    top: 1002px;
    margin: 0;
    transform: translate(-50%, -50%);
    font-family: "Bebas Neue", sans-serif;
    font-size: 78px;
    line-height: 0.95;
    text-align: center;
    color: var(--stamp-green);
  }
  .base-band {
    position: absolute;
    left: 0;
    bottom: 0;
    width: 1200px;
    height: 15px;
    background: var(--gold);
  }
</style>
</head>
<body>
  <main class="label">
    <div class="ornament-band" role="img" aria-label="Row of five faint gold floral line ornaments across the label"></div>

    <h1 class="brand-name">Brambrel</h1>
    <p class="brand-suffix">CANDLE CO.</p>

    <p class="claims">HAND POURED<span class="divider">|</span>ALL NATURAL SOY</p>
    <div class="double-rule"></div>

    <p class="scent-caption">SCENT</p>
    <svg class="scent-stamp" viewBox="0 0 296 296" aria-hidden="true">
      <circle cx="148" cy="148" r="145" fill="none" stroke="var(--gold-faint)" stroke-width="4"/>
    </svg>
    <p class="scent-name">SCENT<br>NAME</p>

    <div class="base-band"></div>
  </main>
</body>
</html>
```